The Pixel Tap Business card.

A Simple card with our Logo and contact information. To give to investors and other professionals.

We are a nerd themed bar.
our target market is young professionals age 21+ but the real purpose of this business card is to present to potential investors and other professionals with our contact information. as we are still looking for funding before we start up.

I am partial to green and my partner likes red we are open to iteration.

Target Market(s)

Investors

Industry/Entity Type

Business

Contact Information for Business Card

Martin Hale (225) 730-6192 kent.h4711@mailnest.test Glen Porter (225) 968-5037 glenp318@mailnest.test

Font styles to use
Serif

Requirements
Nice to have
• Keep it simple but not boring.
• Use the Logos but feel free to edit them to match theme/colors.
• Keep the back clean and use one of the Logos.

```html
<!DOCTYPE html>
<html lang="en">
<head>
<meta charset="utf-8">
<title>The Pixel Tap – Business Card</title>
<link rel="stylesheet" href="https://fonts.googleapis.com/css2?family=Arimo:wght@400&display=swap">
<style>
  :root {
    --canvas: #dcd7cf;
    --card-white: #f7f7f7;
    --card-black: #050505;
    --accent-red: #d9202c;
    --ink: #2b2b2b;
    --ink-soft: #555555;
    --paper-white: #ffffff;
  }
  * { box-sizing: border-box; margin: 0; padding: 0; }
  html, body { width: 1200px; height: 1023px; overflow: hidden; }
  body { background: var(--canvas); position: relative; font-family: "Arimo", Arial, sans-serif; }

  .card {
    position: absolute;
    width: 600px;
    height: 343px;
    border-radius: 4px;
    overflow: hidden;
    box-shadow: 0 12px 28px rgba(0,0,0,.28);
  }

  /* Brand name */
  .brand {
    position: absolute;
    display: flex; align-items: center; gap: 10px;
    white-space: nowrap;
  }
  .brand-mark { width: 14px; height: 14px; background: var(--accent-red); flex: none; }
  .brand-name {
    font-family: "Arimo", Arial, sans-serif; font-weight: 400;
    font-size: 30px; line-height: 1; color: var(--ink);
  }

  /* ---------- Front ---------- */
  .card-front { left: 70px; top: 80px; background: var(--card-white); }
  .card-front .brand { left: 34px; top: 52px; }

  .front-side-strip {
    position: absolute; right: 0; top: 0;
    width: 36px; height: 100%;
    background: var(--card-black);
  }
  .front-bottom-tab {
    position: absolute; right: 36px; bottom: 0;
    width: 250px; height: 16px;
    background: var(--accent-red);
    border-radius: 12px 12px 0 0;
  }

  .contact-block {
    position: absolute; right: 56px;
    text-align: right; font-size: 13.5px; line-height: 22px; color: var(--ink-soft);
  }
  .contact-block.primary { top: 30px; }
  .contact-block.secondary { top: 150px; }
  .contact-line { display: flex; justify-content: flex-end; align-items: center; gap: 8px; }
  .contact-icon { width: 14px; height: 14px; flex: none; }

  .divider {
    position: absolute; left: 34px; right: 80px; top: 128px;
    height: 2px; background: var(--accent-red);
  }

  .person { position: absolute; left: 34px; top: 262px; }
  .person-name { font-size: 22px; color: var(--ink); line-height: 1.1; }
  .person-role { font-size: 14px; color: var(--ink-soft); margin-top: 2px; }

  /* ---------- Back ---------- */
  .card-back { left: 530px; top: 600px; background: var(--card-black); }
  .card-back .brand { left: 50%; top: 50%; transform: translate(-50%, -50%); }
  .card-back .brand-name { color: var(--paper-white); font-size: 36px; }
</style>
</head>
<body>

<section class="card card-front" aria-label="Business card front">
  <div class="front-side-strip"></div>
  <div class="front-bottom-tab"></div>

  <div class="brand">
    <span class="brand-mark"></span>
    <span class="brand-name">The Pixel Tap</span>
  </div>

  <div class="contact-block primary">
    <div class="contact-line">(225) 730-6192 (Martin Hale)
      <svg class="contact-icon" viewBox="0 0 14 14"><rect width="14" height="14" rx="2" fill="#d9202c"/><path d="M4.2 3.2h2l.6 2-1 .8a5 5 0 0 0 2.2 2.2l.8-1 2 .6v2a1 1 0 0 1-1 1A7 7 0 0 1 3.2 4.2a1 1 0 0 1 1-1z" fill="#fff"/></svg>
    </div>
    <div class="contact-line">kent.h4711@mailnest.test
      <svg class="contact-icon" viewBox="0 0 14 14"><rect width="14" height="14" rx="2" fill="#d9202c"/><rect x="3" y="4" width="8" height="6" fill="none" stroke="#fff" stroke-width="1"/><path d="M3 4l4 3.2L11 4" fill="none" stroke="#fff" stroke-width="1"/></svg>
    </div>
  </div>

  <div class="divider"></div>

  <div class="contact-block secondary">
    <div class="contact-line">(225) 968-5037 (Glen Porter)
      <svg class="contact-icon" viewBox="0 0 14 14"><rect width="14" height="14" rx="2" fill="#d9202c"/><path d="M4.2 3.2h2l.6 2-1 .8a5 5 0 0 0 2.2 2.2l.8-1 2 .6v2a1 1 0 0 1-1 1A7 7 0 0 1 3.2 4.2a1 1 0 0 1 1-1z" fill="#fff"/></svg>
    </div>
    <div class="contact-line">glenp318@mailnest.test
      <svg class="contact-icon" viewBox="0 0 14 14"><rect width="14" height="14" rx="2" fill="#d9202c"/><rect x="3" y="4" width="8" height="6" fill="none" stroke="#fff" stroke-width="1"/><path d="M3 4l4 3.2L11 4" fill="none" stroke="#fff" stroke-width="1"/></svg>
    </div>
  </div>

  <div class="person">
    <div class="person-name">Martin Hale</div>
    <div class="person-role">Founder</div>
  </div>
</section>

<section class="card card-back" aria-label="Business card back">
  <div class="brand">
    <span class="brand-mark"></span>
    <span class="brand-name">The Pixel Tap</span>
  </div>
</section>

</body>
</html>
```